Brivo Packworks Website using Wix Platform

Project Overview:
Brivo Packworks is a supply chain company specializing in packaging and manufacturing services for CPG (Consumer Packaged Goods) brands and nutritional/dietary supplement companies. The company offers end-to-end solutions including packaging design, production, co-packing, and private labeling. The goal of this project is to create a professional, user-friendly website that showcases your expertise, builds trust with potential clients, and generates leads for your services.

Objectives:
Establish Brand Authority: Position Brivo Packworks as a leader in the packaging and manufacturing industry for CPG and nutritional products.
Lead Generation: Encourage visitors to contact you for quotes, consultations, or further information.
Professional User Experience: Ensure the website is easy to navigate, visually appealing, and mobile-friendly.
SEO & Conversion Optimization: Optimize the site for search engines to attract organic traffic and improve conversion rates.
Primary Audience:
CPG Brands: Companies in industries like food and beverage, personal care, and household products looking for packaging and manufacturing services.
Nutritional/Dietary Supplement Brands: Companies in the health and wellness industry needing specialized packaging and manufacturing services for supplements, including compliance with regulatory standards (GMP).
Secondary Audience:
Potential partners looking to collaborate on co-packing or private labeling.
Key Features & Functionality:
Responsive Design:

The website must be fully responsive, ensuring optimal viewing across all devices (desktops, tablets, mobile).
User-Centric Navigation:

A clean, intuitive navigation system that allows users to quickly access key pages such as Home, Services, About Us, Case Studies, FAQ, and Contact.
Lead Generation Forms:

Prominent CTAs (Calls to Action) throughout the website encouraging users to “Request a Quote”, “Get in Touch”, or “Learn More” about your services.
Contact Form: Simple form allowing potential clients to submit inquiries about your services.
SEO Optimization:

The site should be optimized for relevant keywords (e.g., “co-packing services for CPG,” “nutritional supplement packaging,” “custom packaging solutions”), including meta descriptions, headers, and on-page content.
Content Management System (CMS):

An easy-to-use CMS (like WordPress or Webflow) for easy content updates. This will allow you to make changes to your services, case studies, and other sections without requiring a developer.
Analytics Integration:

Google Analytics or a similar tool for tracking site visitors and performance metrics to make data-driven decisions on site improvements.
Site Structure & Content:
1. Home Page:
Hero Section with tagline, images or video of your services in action, and a clear CTA (e.g., “Request a Quote”).
Value Proposition: Short and compelling introduction to Brivo Packworks’s core services and advantages.
Overview of Services: Highlight your key offerings (e.g., Packaging Design, Co-packing, Nutritional Supplement Packaging, Private Labeling).
Client Logos/Testimonials: Social proof to establish credibility.
CTA Buttons: Throughout the page to drive conversions (e.g., “Get a Free Consultation”).
2. About Us Page:
Company Overview: Explain your mission, values, and commitment to quality.
Team Overview (Optional): Introduce key team members to humanize your company and build trust.
Core Values and Differentiators: Showcase what makes Brivo Packworks unique—sustainability practices, regulatory compliance, and industry expertise.
3. Services Pages (Separate Pages for Each Service):
Packaging & Design: Custom packaging solutions, materials, and design services for CPG brands.
Manufacturing & Assembly: Your end-to-end production process, assembly capabilities, and how you support both small and large-scale runs.
Nutritional & Dietary Supplement Packaging: Focus on specialized packaging for supplements, regulatory compliance (GMP), and certifications.
Private Labeling: Services for clients who wish to brand their own products using your packaging.
Each service page will include detailed descriptions, benefits, process information, and CTAs like “Get Started” or “Request a Quote”.
4. Case Studies / Portfolio Page:
Success Stories: Showcase in-depth case studies of past projects, especially successful partnerships with CPG or supplement brands.
Before & After Images: Display the difference your services have made for clients, especially in terms of packaging quality or branding improvements.
Client Testimonials: Additional customer feedback to strengthen your brand reputation.
5. FAQ Page:
Address common questions related to lead times, regulatory compliance, order quantities, and specific details for different industries (e.g., dietary supplements).
The format will be accordion-style or dropdowns for easy scanning.
6. Contact Us Page:
Contact Form: With fields for name, email, company, and inquiry details.
Location Information: Physical address, phone number, and working hours.
Map Integration: If relevant, integrate Google Maps to show your office location.
Social Media Links: Link to your company’s LinkedIn, Instagram, or other relevant platforms.

Target Market(s)

Startup CPG Brands, Supplement Brands, Nutrition Brands

Industry/Entity Type

Flexible Packaging, Contract Manufacturing, Supplement & Food Manufacturing

Coding

Coded - Design and coding required

Number of Pages Required

5+ page

Requirements
Must have
• Use our colors.
Nice to have
• https://tornap482.sitebuildhost.example/brivopackworks - www.ninefoldlane.example - www.pelkasnacks.example - thebrightmill.example

```html
<!DOCTYPE html>
<html lang="en">
<head>
<meta charset="utf-8">
<title>Brivo Packworks — Simplify the Process</title>
<link href="https://fonts.googleapis.com/css2?family=League+Spartan:wght@400;500;600;700&family=Montserrat:wght@400;500;600;700&display=swap" rel="stylesheet">
<style>
:root{
  --navy:#0b1650;
  --navy-deep:#08103e;
  --blue:#1ba6e0;
  --green:#9ccb3b;
  --green-dark:#7fb02a;
  --ink:#1b1f3b;
  --muted:#4a4f68;
  --pale:#eef6fb;
  --white:#ffffff;
}
*{margin:0;padding:0;box-sizing:border-box}
html,body{width:1200px;height:5254px;overflow:hidden}
body{position:relative;font-family:"Montserrat",sans-serif;color:var(--ink);background:var(--white)}
.abs{position:absolute}
.display{font-family:"League Spartan",sans-serif;font-weight:700;text-transform:uppercase}
.btn{position:absolute;display:flex;align-items:center;justify-content:center;border-radius:30px;font-family:"League Spartan",sans-serif;font-weight:600;text-transform:uppercase;letter-spacing:.3px}
.btn-green{background:var(--green);color:var(--navy)}
.btn-blue{background:var(--blue);color:var(--white)}
.btn-navy{background:var(--navy);color:var(--white)}
.photo{position:absolute}

/* header / hero */
.hero{position:absolute;left:0;top:0;width:1200px;height:730px}
.hero-bg{position:absolute;left:0;top:0}
.brand{position:absolute;font-family:"League Spartan",sans-serif;font-weight:600;color:var(--white);font-size:25px;letter-spacing:.5px}
.nav{position:absolute;left:394px;top:37px;display:flex;align-items:center;font-family:"League Spartan",sans-serif;font-weight:500;font-size:13px;color:var(--white);text-transform:uppercase}
.nav a{color:var(--white);text-decoration:none;padding:0 24px;border-left:1px solid rgba(255,255,255,.35)}
.nav a:first-child{padding-left:0;border-left:none;position:relative}
.nav a.active::after{content:"";position:absolute;left:0;right:24px;bottom:-8px;height:2px;background:var(--green)}
.nav-contact{position:absolute;left:929px;top:27px;width:122px;height:36px;border:2px solid var(--white);border-radius:20px;color:var(--white);font-family:"League Spartan",sans-serif;font-weight:500;font-size:13px;display:flex;align-items:center;justify-content:center}
.hero-kicker{position:absolute;left:124px;top:222px;color:var(--white);font-family:"League Spartan",sans-serif;font-weight:500;font-size:22px;display:flex;align-items:center;gap:10px}
.hero-kicker::after{content:"";width:54px;height:2px;background:var(--green)}
.hero-title{position:absolute;left:116px;top:258px;font-size:66px;line-height:64px;color:var(--white)}
.hero-title span{color:var(--blue)}

/* intro */
.section-kicker{font-family:"League Spartan",sans-serif;font-weight:600;text-transform:uppercase;color:var(--blue)}
.rule{position:absolute;height:3px;width:50px;background:var(--green)}
.intro-copy{position:absolute;left:220px;top:914px;width:760px;text-align:center;font-size:15.5px;line-height:22px;color:var(--muted)}
.adv{position:absolute;width:260px}
.adv h4{font-family:"League Spartan",sans-serif;font-weight:600;font-size:17px;color:var(--ink);margin-bottom:3px}
.adv p{font-size:10.5px;line-height:15px;color:var(--muted)}
.adv.right{text-align:right}
.adv-icon{position:absolute;width:72px;height:72px;border-radius:50%;display:flex;align-items:center;justify-content:center}
.adv-icon.blue{background:var(--blue)}
.adv-icon.green{background:var(--green)}

/* services */
.services{position:absolute;left:0;top:1714px;width:1200px;height:1484px;background:var(--pale)}
.card{position:absolute;background:var(--white)}
.card h3{font-family:"League Spartan",sans-serif;font-weight:600;font-size:26px;text-transform:uppercase;color:var(--ink);line-height:34px}
.card p{font-size:14.5px;line-height:21px;color:var(--ink);margin-top:8px}
.card .btn{position:static;display:inline-flex;margin-top:14px;width:150px;height:34px;font-size:13px}
.card-body{position:absolute;left:38px;right:34px}
.accent{position:absolute}

/* clients */
.client{position:absolute;font-family:"League Spartan",sans-serif;font-weight:600;font-size:20px;color:var(--navy);text-align:center;width:170px}
.dots{position:absolute;left:534px;top:3530px;display:flex;gap:10px}
.dots span{width:42px;height:3px;background:#c4d7ea}
.dots span:first-child{background:var(--blue)}

/* testimonials */
.testi{position:absolute;left:0;top:3618px;width:1200px;height:586px;background:linear-gradient(100deg,#ffffff 0%,#f0f7fb 50%,#dbeef7 100%)}
.quote-card{position:absolute;top:3820px;width:325px;height:290px;background:var(--white);border:1px solid #e1e6ee;padding:30px 40px}
.quote-mark{font-family:"League Spartan",sans-serif;font-weight:700;font-size:70px;line-height:50px;color:var(--green);height:44px}
.quote-card p{font-size:12.5px;line-height:22px;color:var(--muted);margin-top:14px}
.quote-card h5{font-family:"League Spartan",sans-serif;font-weight:600;font-size:18px;margin-top:22px;color:var(--ink)}
.quote-card small{display:block;font-size:10px;color:var(--blue);margin-top:4px}
.arrow{position:absolute;top:3947px;width:36px;height:36px;border-radius:50%;background:var(--blue);display:flex;align-items:center;justify-content:center}

/* consultation */
.consult{position:absolute;left:126px;top:4275px;width:976px;height:545px;background:var(--blue);overflow:hidden}
.field{position:absolute;background:var(--white);font-size:11.5px;color:var(--muted);padding:12px 16px}

/* footer */
.footer{position:absolute;left:0;top:4887px;width:1200px;height:367px;background:var(--navy-deep)}
.fcol{position:absolute;top:80px;padding-left:18px;border-left:1px solid rgba(255,255,255,.3);height:210px}
.fcol h6{font-family:"League Spartan",sans-serif;font-weight:600;font-size:15px;color:var(--white);text-transform:uppercase;margin-bottom:14px;letter-spacing:.5px}
.fcol li{list-style:none;font-size:13px;color:var(--white);line-height:26px}
.social{position:absolute;top:140px;left:186px;display:flex;gap:10px}
.social span{width:24px;height:24px;border-radius:50%;background:var(--white)}
.contact-row{display:flex;align-items:center;gap:14px;margin-bottom:18px}
.contact-row i{width:32px;height:32px;border-radius:50%;background:var(--green);display:flex;align-items:center;justify-content:center}
.contact-row small{display:block;font-size:10.5px;color:var(--white)}
.contact-row b{font-weight:500;font-size:13.5px;color:var(--white)}
.copyright{position:absolute;left:0;top:296px;width:1200px;border-top:1px solid rgba(255,255,255,.2);padding-top:28px;text-align:center;font-size:11px;color:var(--white)}
</style>
</head>
<body>

<!-- HERO -->
<header class="hero">
  <svg class="hero-bg" width="1200" height="730" viewBox="0 0 1200 730">
    <defs>
      <linearGradient id="heroGrad" x1="0" y1="0" x2="1" y2="1">
        <stop offset="0" stop-color="#0a1650"/>
        <stop offset="1" stop-color="#0d1d6b"/>
      </linearGradient>
    </defs>
    <path d="M0,0 H1200 V610 Q700,760 0,580 Z" fill="url(#heroGrad)"/>
    <path d="M0,580 Q700,760 1200,610 L1200,622 Q700,770 0,600 Z" fill="#1ba6e0"/>
    <path d="M0,600 Q700,770 1200,622 L1200,632 Q700,745 0,600 Z" fill="#9ccb3b"/>
  </svg>
  <div class="brand" style="left:114px;top:30px">BRIVO PACKWORKS</div>
  <nav class="nav">
    <a class="active">Home</a><a>Services</a><a>About Us</a><a>Case Studies</a><a>FAQ</a>
  </nav>
  <div class="nav-contact">CONTACT</div>
  <div class="hero-kicker">BRIVO PACKWORKS</div>
  <h1 class="hero-title display">Simplify the<br><span>Process</span></h1>
  <div class="btn btn-green" style="left:114px;top:418px;width:232px;height:58px;font-size:17px">Request a Quote</div>
  <div class="photo" role="img" aria-label="Two kraft paper coffee bags standing side by side" style="left:590px;top:130px;width:522px;height:470px;background:radial-gradient(ellipse at 45% 50%,#d9c3a2 0%,#c4a57e 40%,rgba(13,29,107,0) 72%)"></div>
</header>

<!-- INTRO -->
<section>
  <div class="abs section-kicker" style="left:0;top:796px;width:1200px;text-align:center;font-size:28px">Introduction to</div>
  <h2 class="abs display" style="left:0;top:832px;width:1200px;text-align:center;font-size:44px;color:var(--ink)">Brivo Packworks</h2>
  <div class="rule" style="left:576px;top:886px"></div>
  <p class="intro-copy">Lorem ipsum dolor sit amet, consectetur adipiscing elit sed do eiusmod tempor incididunt ut labore et dolore magna aliqua. Quis ipsum suspendisse ultrices gravida. Risus commodo viverra maecenas accumsan lacus vel facilisis.</p>

  <svg class="abs" style="left:402px;top:1004px" width="400" height="400" viewBox="0 0 400 400">
    <defs>
      <radialGradient id="advGrad" cx="0.5" cy="0.45" r="0.55">
        <stop offset="0" stop-color="#8fc33a"/>
        <stop offset="1" stop-color="#6fa623"/>
      </radialGradient>
    </defs>
    <circle cx="200" cy="200" r="188" fill="none" stroke="#1ba6e0" stroke-width="2"/>
    <circle cx="200" cy="200" r="168" fill="#ffffff" stroke="#9ccb3b" stroke-width="6"/>
    <circle cx="200" cy="200" r="158" fill="url(#advGrad)"/>
    <circle cx="55" cy="98" r="6" fill="#fff" stroke="#1ba6e0" stroke-width="2"/>
    <circle cx="345" cy="98" r="6" fill="#fff" stroke="#1ba6e0" stroke-width="2"/>
    <circle cx="25" cy="255" r="6" fill="#fff" stroke="#1ba6e0" stroke-width="2"/>
    <circle cx="375" cy="255" r="6" fill="#fff" stroke="#1ba6e0" stroke-width="2"/>
    <text x="200" y="200" text-anchor="middle" font-family="League Spartan, sans-serif" font-weight="700" font-size="70" fill="#ffffff">BRIVO</text>
    <text x="200" y="213" text-anchor="middle" dy="26" font-family="League Spartan, sans-serif" font-weight="600" font-size="26" fill="#ffffff">ADVANTAGES</text>
  </svg>

  <div class="adv-icon blue" style="left:352px;top:1036px">
    <svg width="34" height="34" viewBox="0 0 34 34" fill="none" stroke="#fff" stroke-width="2"><circle cx="17" cy="14" r="8"/><path d="M13 23h8M14 27h6M17 2v3M5 14H2M32 14h-3"/></svg>
  </div>
  <div class="adv right" style="left:80px;top:1044px"><h4>Custom Solutions</h4><p>Lorem ipsum dolor sit amet, consectetur adipiscing eli Lorem ipsum dolor sit amet consectetur</p></div>

  <div class="adv-icon blue" style="left:770px;top:1041px">
    <svg width="36" height="34" viewBox="0 0 36 34" fill="none" stroke="#fff" stroke-width="2"><circle cx="18" cy="11" r="5"/><circle cx="7" cy="15" r="3.5"/><circle cx="29" cy="15" r="3.5"/><path d="M9 30c0-6 4-10 9-10s9 4 9 10M1 28c0-4 2-7 6-7M35 28c0-4-2-7-6-7"/></svg>
  </div>
  <div class="adv" style="left:855px;top:1038px"><h4>Expert Team</h4><p>Lorem ipsum dolor sit amet, consectetur adipiscing eli Lorem ipsum dolor sit amet consectetur</p></div>

  <div class="adv-icon green" style="left:344px;top:1282px">
    <svg width="36" height="34" viewBox="0 0 36 34" fill="none" stroke="#fff" stroke-width="2"><circle cx="20" cy="17" r="12"/><path d="M20 10v7l5 3M2 12h8M4 18h6M2 24h8"/></svg>
  </div>
  <div class="adv right" style="left:70px;top:1287px"><h4>Fast Turnaround</h4><p>Lorem ipsum dolor sit amet, consectetur adipiscing eli Lorem ipsum dolor sit amet consectetur</p></div>

  <div class="adv-icon green" style="left:776px;top:1290px">
    <svg width="34" height="34" viewBox="0 0 34 34" fill="none" stroke="#fff" stroke-width="2"><path d="M17 3l10 4v8c0 7-5 12-10 15C12 27 7 22 7 15V7z"/><path d="M12 16l4 4 7-8"/></svg>
  </div>
  <div class="adv" style="left:861px;top:1295px"><h4>Quality &amp; Compliance</h4><p>Lorem ipsum dolor sit amet, consectetur adipiscing eli Lorem ipsum dolor sit amet consectetur</p></div>

  <div class="adv-icon blue" style="left:570px;top:1396px">
    <svg width="34" height="34" viewBox="0 0 34 34" fill="none" stroke="#fff" stroke-width="2"><path d="M17 3l12 6v14l-12 7-12-7V9z"/><path d="M5 9l12 7 12-7M17 16v14"/></svg>
  </div>
  <div class="adv" style="left:456px;top:1484px;width:300px;text-align:center"><h4>Flexible Packaging</h4><p>Lorem ipsum dolor sit amet, consectetur adipiscing eli Lorem ipsum dolor sit amet</p></div>

  <div class="btn btn-navy" style="left:471px;top:1574px;width:280px;height:60px;font-size:15px">Get a Free Consultation</div>
</section>

<!-- SERVICES -->
<section class="services">
  <div class="abs section-kicker" style="left:110px;top:82px;font-size:29px">Our Key Offering</div>
  <h2 class="abs display" style="left:110px;top:118px;font-size:46px;color:var(--ink)">Services</h2>
  <div class="rule" style="left:112px;top:172px;width:58px"></div>
</section>

<!-- card: packaging design -->
<div class="accent" style="left:94px;top:2295px;width:9px;height:175px;background:var(--green)"></div>
<div class="accent" style="left:94px;top:2461px;width:206px;height:9px;background:var(--green)"></div>
<div class="card" style="left:108px;top:1938px;width:480px;height:521px">
  <div class="photo" role="img" aria-label="Pantry groceries including cooking oil, canned goods, rice and vegetables on a red backdrop" style="left:0;top:0;width:480px;height:327px;background:linear-gradient(180deg,#c4161c 0%,#d8342a 60%,#e7a46b 100%)"></div>
  <div class="card-body" style="top:350px">
    <h3>Packaging Design</h3>
    <p>Lorem ipsum dolor sit amet, consectetur adipiscing elit, sed do eiusmod tempor incididunt</p>
    <div class="btn btn-green">Learn More</div>
  </div>
</div>

<!-- card: co-packing -->
<div class="accent" style="left:1103px;top:2290px;width:9px;height:80px;background:var(--blue)"></div>
<div class="accent" style="left:834px;top:2361px;width:278px;height:9px;background:var(--blue)"></div>
<div class="card" style="left:626px;top:1843px;width:482px;height:518px">
  <div class="photo" role="img" aria-label="Black cosmetic cartons arranged on a light grey surface" style="left:0;top:0;width:482px;height:327px;background:linear-gradient(135deg,#e7e7e7 0%,#cfcfcf 45%,#2a2a2a 46%,#3a3a3a 100%)"></div>
  <div class="card-body" style="top:350px">
    <h3>Co-Packing</h3>
    <p>Lorem ipsum dolor sit amet, consectetur adipiscing elit, sed do eiusmod tempor incididunt</p>
    <div class="btn btn-green">Learn More</div>
  </div>
</div>

<!-- card: private labeling -->
<div class="accent" style="left:94px;top:2950px;width:9px;height:90px;background:var(--blue)"></div>
<div class="accent" style="left:94px;top:3031px;width:290px;height:9px;background:var(--blue)"></div>
<div class="card" style="left:108px;top:2512px;width:480px;height:518px">
  <div class="photo" role="img" aria-label="Two colourful supplement bottles on a warm beige background" style="left:0;top:0;width:480px;height:329px;background:linear-gradient(120deg,#e6c9a3 0%,#d9b387 55%,#c79a6c 100%)"></div>
  <div class="card-body" style="top:350px">
    <h3>Private Labeling</h3>
    <p>Lorem ipsum dolor sit amet, consectetur adipiscing elit, sed do eiusmod tempor incididunt</p>
    <div class="btn btn-green">Learn More</div>
  </div>
</div>

<!-- card: nutritional supplement -->
<div class="accent" style="left:1108px;top:2820px;width:9px;height:162px;background:var(--green)"></div>
<div class="accent" style="left:968px;top:2973px;width:149px;height:9px;background:var(--green)"></div>
<div class="card" style="left:626px;top:2424px;width:482px;height:549px">
  <div class="photo" role="img" aria-label="Kraft and white supplement boxes standing on a neutral surface" style="left:0;top:0;width:482px;height:330px;background:linear-gradient(135deg,#d8d2c8 0%,#c7baa6 50%,#a98a66 100%)"></div>
  <div class="card-body" style="top:346px">
    <h3>Nutritional<br>Supplement Packaging</h3>
    <p>Lorem ipsum dolor sit amet, consectetur adipiscing elit, sed do eiusmod tempor incididunt</p>
    <div class="btn btn-green">Learn More</div>
  </div>
</div>

<div class="btn btn-blue" style="left:482px;top:3084px;width:236px;height:60px;font-size:16px">Request a Quote</div>

<!-- CLIENTS -->
<section>
  <h2 class="abs display" style="left:0;top:3280px;width:1200px;text-align:center;font-size:38px;color:var(--ink)"><span style="color:var(--blue)">Meet</span> Our Clients</h2>
  <div class="rule" style="left:572px;top:3330px;width:58px"></div>
  <div class="client" style="left:108px;top:3416px">Northdale Law</div>
  <div class="client" style="left:308px;top:3416px">Prismvale</div>
  <div class="client" style="left:508px;top:3416px">Slotwick</div>
  <div class="client" style="left:716px;top:3416px">Harlow &amp; Finn</div>
  <div class="client" style="left:916px;top:3416px">Clearpoint Legal</div>
  <div class="dots"><span></span><span></span><span></span></div>
</section>

<!-- TESTIMONIALS -->
<section class="testi"></section>
<div class="abs section-kicker" style="left:0;top:3684px;width:1200px;text-align:center;font-size:22px">Testimonials</div>
<h2 class="abs display" style="left:0;top:3716px;width:1200px;text-align:center;font-size:38px;font-weight:500;color:var(--ink)">What Our Client Says</h2>
<div class="rule" style="left:576px;top:3762px"></div>

<div class="accent" style="left:104px;top:3808px;width:100px;height:9px;background:var(--green)"></div>
<div class="accent" style="left:104px;top:3808px;width:9px;height:74px;background:var(--green)"></div>
<div class="accent" style="left:1030px;top:4116px;width:104px;height:9px;background:var(--green)"></div>
<div class="accent" style="left:1125px;top:4040px;width:9px;height:85px;background:var(--green)"></div>

<div class="quote-card" style="left:112px">
  <div class="quote-mark">&ldquo;</div>
  <p>“I would like to acknowledge the efforts, encouragement, and advice of Dorian and other individuals that help to make the Oakhollow Foods launch happen.”</p>
  <h5>Marla Quenby, PhD</h5><small>President &amp; Founder, Oakhollow Foods</small>
</div>
<div class="quote-card" style="left:455px">
  <div class="quote-mark">&ldquo;</div>
  <p>“I would like to acknowledge the efforts, encouragement, and advice of Dorian and other individuals that help to make the Oakhollow Foods launch happen.”</p>
  <h5>Marla Quenby, PhD</h5><small>President &amp; Founder, Oakhollow Foods</small>
</div>
<div class="quote-card" style="left:798px">
  <div class="quote-mark">&ldquo;</div>
  <p>“I would like to acknowledge the efforts, encouragement, and advice of Dorian and other individuals that help to make the Oakhollow Foods launch happen.”</p>
  <h5>Marla Quenby, PhD</h5><small>President &amp; Founder, Oakhollow Foods</small>
</div>
<div class="arrow" style="left:57px"><svg width="16" height="16" viewBox="0 0 16 16" fill="none" stroke="#fff" stroke-width="2"><path d="M14 8H3M7 3L2 8l5 5"/></svg></div>
<div class="arrow" style="left:1135px"><svg width="16" height="16" viewBox="0 0 16 16" fill="none" stroke="#fff" stroke-width="2"><path d="M2 8h11M9 3l5 5-5 5"/></svg></div>

<!-- CONSULTATION -->
<div class="accent" style="left:112px;top:4262px;width:146px;height:8px;background:var(--blue)"></div>
<div class="accent" style="left:112px;top:4262px;width:8px;height:110px;background:var(--blue)"></div>
<div class="accent" style="left:975px;top:4827px;width:140px;height:8px;background:var(--green)"></div>
<div class="accent" style="left:1107px;top:4745px;width:8px;height:90px;background:var(--green)"></div>

<section class="consult">
  <div class="photo" role="img" aria-label="Smiling man in glasses and denim shirt holding a tablet" style="left:0;top:0;width:500px;height:545px;clip-path:polygon(0 0,420px 0,330px 545px,0 545px);background:linear-gradient(135deg,#b6d84a 0%,#9ccb3b 50%,#7fb02a 100%)"></div>
  <div class="abs" style="left:116px;top:248px;width:248px;height:54px;background:#fff;display:flex;align-items:center;justify-content:center;font-family:'League Spartan',sans-serif;font-weight:600;font-size:21px;color:var(--navy)">BRIVO PACKWORKS</div>
  <h2 class="abs display" style="left:478px;top:104px;font-size:36px;line-height:38px;font-weight:600;color:#fff">Get a Free<br>Consultation</h2>
  <div class="field" style="left:482px;top:198px;width:214px;height:42px">First Name</div>
  <div class="field" style="left:709px;top:198px;width:216px;height:42px">Last Name</div>
  <div class="field" style="left:482px;top:255px;width:214px;height:42px">Email address</div>
  <div class="field" style="left:709px;top:255px;width:216px;height:42px">Phone number</div>
  <div class="field" style="left:482px;top:312px;width:443px;height:92px">Message</div>
  <div class="btn btn-navy" style="left:482px;top:419px;width:170px;height:38px;font-size:13px">Send Message</div>
</section>

<!-- FOOTER -->
<footer class="footer">
  <div class="brand" style="left:137px;top:88px;font-size:26px">BRIVO PACKWORKS</div>
  <div class="social" aria-label="Social media links"><span></span><span></span><span></span><span></span><span></span></div>
  <div class="fcol" style="left:416px">
    <h6>Navigation</h6>
    <ul><li>Home</li><li>Services</li><li>About Us</li><li>Case Studies</li></ul>
  </div>
  <div class="fcol" style="left:639px">
    <h6>Resources</h6>
    <ul><li>FAQ</li><li>Terms of Use</li><li>Contact</li></ul>
  </div>
  <div class="fcol" style="left:839px">
    <h6>Contact Us</h6>
    <div class="contact-row"><i><svg width="14" height="14" viewBox="0 0 24 24" fill="#0b1650"><path d="M6.6 10.8a15 15 0 006.6 6.6l2.2-2.2a1 1 0 011-.25 11.4 11.4 0 003.6.6 1 1 0 011 1V20a1 1 0 01-1 1A17 17 0 013 4a1 1 0 011-1h3.5a1 1 0 011 1c0 1.25.2 2.45.6 3.6a1 1 0 01-.25 1z"/></svg></i><div><small>Phone Number</small><b>(555) 214-7730</b></div></div>
    <div class="contact-row"><i><svg width="14" height="14" viewBox="0 0 24 24" fill="#0b1650"><path d="M2 5h20v14H2z"/><path d="M2 5l10 8 10-8" stroke="#9ccb3b" stroke-width="2" fill="none"/></svg></i><div><small>Email Us</small><b>enquiry@brivopackworks.example</b></div></div>
  </div>
  <div class="copyright">Copyright © 2024 <u>Brivo Packworks</u>. All Right Reserved</div>
</footer>

</body>
</html>
```